brevakor.com

I have a site already disigned, however at the time I had no clue of how and what my site should look like. Still pretty cluless but I know I need to make some fundamenlal changes. I'm looking fora designer who understands how to connect with the cosumer with a ballance of visual and content with SEO in mind.I have a lot of content ready to be added to the mix, just missing alot of bottons for the content for example I have FAQ content but no FAQ botton. There are a lot of things I would like to add and take away from the current site. Here is a list of what I would like to add and subtracted from the site.Take away the find botton and ad contact us change the about botton to about brevakor,under that botton i want bottons that lead to News/Events,carreer opertunities,contact us and priacy policy. I also want to add Services offered: personal training,Motivational speeking ,bootcamp conditioning,rondalo,kickboxing cardio,and hip hop cordio. I want to add a botton for testimonials:video and written. I need to add a blog botton, a FAQ botton, and before and after. I want to add a social media botton: chatterloop, snapvelle,quibbler,hirenook,clipstream,and map corner. I need to add a store botton; T shirts. I would like the contact info the be linked to my email. and I would like would like at the top of contact form to read Request a free info session Now!!! But I don't need a new design I need to add these thing to the one I already have whitch is CMS based

Reason: I need my site to have new logo, just figured out how to down load logo

Reason: I need site to be CMS based so I can up load content and pics

Target Market(s)

People who want to loose weight, mostley women over the age of 30 and men over the age of 40 that income is at least 60,000 a year

Industry/Entity Type

Store

Font styles to use
Sans Serif
Decorative

Colors
000000
ec1f27
0255a3

Requirements
Must have
• Adding the drop downs listed above

```html
<!DOCTYPE html>
<html lang="en">
<head>
<meta charset="utf-8">
<title>brevakor – Fitness</title>
<link rel="stylesheet" href="https://fonts.googleapis.com/css2?family=Open+Sans:wght@400;600;700&family=Oswald:wght@400;500;700&display=swap">
<style>
:root{
  --red:#c0262c;
  --red-dark:#a41e23;
  --red-bright:#ec1f27;
  --ink:#333333;
  --muted:#8a8a8a;
  --nav:#2c2c2c;
  --band:#333333;
  --footer:#2a2a2a;
  --footer-col:#1f1f1f;
  --panel:#efefef;
  --field:#e2e2e2;
  --white:#ffffff;
}
*{box-sizing:border-box;margin:0;padding:0}
html,body{width:883px;height:1200px;overflow:hidden;background:var(--white)}
body{position:relative;font-family:"Open Sans",Arial,sans-serif;color:var(--ink);font-size:7px}
h2,h3{font-weight:400}
.abs{position:absolute}
/* header */
.site-header{left:0;top:0;width:883px;height:86px;background:var(--white)}
.brand{left:236px;top:4px;width:84px;height:84px;border-radius:50%;background:#1a1a1a;display:flex;align-items:center;justify-content:center;color:var(--white);font-weight:700;font-size:14px;letter-spacing:.5px}
.brand-dot{display:inline-block;width:8px;height:8px;border-radius:50%;background:var(--red-bright);margin-right:5px}
.header-mail{left:612px;top:49px;font-size:7px;color:#555;display:flex;align-items:center;gap:4px}
.header-mail i{display:inline-block;width:8px;height:5px;background:var(--red)}
/* nav */
.main-nav{left:0;top:86px;width:883px;height:29px;background:var(--nav)}
.main-nav ul{position:absolute;left:234px;top:0;width:446px;height:29px;display:flex;justify-content:space-between;align-items:center;list-style:none}
.main-nav li{color:#cfcfcf;font-size:7px;white-space:nowrap}
.main-nav li.active{color:var(--white);font-weight:700}
/* hero */
.hero{left:0;top:115px;width:883px;height:251px;
  background:
    radial-gradient(ellipse 180px 90px at 640px 120px,rgba(240,240,240,.55),rgba(240,240,240,0)),
    radial-gradient(ellipse 90px 60px at 300px 75px,rgba(20,20,20,.6),rgba(20,20,20,0)),
    linear-gradient(180deg,#2b2b2b 0%,#5a5a5a 28%,#8c8c8c 60%,#b4b4b4 100%)}
.phone-tab{left:572px;top:115px;width:106px;height:22px;background:var(--red);color:var(--white);font-size:9px;display:flex;align-items:center;white-space:nowrap}
.phone-tab .ico{flex:none;width:20px;height:22px;display:flex;align-items:center;justify-content:center;background:var(--red-dark);margin-right:12px}
.slide-arrow{top:231px;width:20px;height:20px;border-radius:50%;background:rgba(0,0,0,.45);display:flex;align-items:center;justify-content:center}
.caption-band{left:0;top:366px;width:883px;height:44px;background:var(--band)}
.caption-tag{left:392px;top:341px;width:162px;height:26px;background:var(--red);color:var(--white);font-size:8.5px;display:flex;align-items:center;padding-left:12px;white-space:nowrap}
.caption-text{left:392px;top:379px;width:260px;color:#bdbdbd;font-size:6.5px;line-height:11px}
/* request form */
.request-form{left:234px;top:310px;width:137px;height:214px;background:var(--panel);padding:12px 10px}
.request-form h3{color:var(--red);font-size:7.3px;font-weight:400;margin-bottom:7px;white-space:nowrap}
.request-form p{color:#777;font-size:5.5px;line-height:8px;margin-bottom:9px}
.field{height:16px;background:var(--field);margin:0 0 3px 2px;width:113px;color:#9a9a9a;font-size:5px;padding:0 6px;display:flex;align-items:center;justify-content:space-between}
.field.msg{height:38px;align-items:flex-start;padding-top:5px}
.book-btn{margin:5px 0 0 2px;width:113px;height:21px;background:var(--red);color:var(--white);font-size:6.5px;font-weight:700;display:flex;align-items:center;justify-content:center}
/* welcome */
.welcome-title{left:392px;top:438px;color:var(--red);font-size:9.5px}
.welcome-photo{left:392px;top:466px;width:95px;height:57px;background:linear-gradient(135deg,#9fd0e8,#3b86b8 60%,#e6c9a9)}
.welcome-text{left:503px;top:465px;width:172px;font-size:5.6px;line-height:8.6px;color:#666}
.welcome-text b{color:var(--red);font-weight:600}
/* columns */
.col-title{top:550px;font-size:9.5px;color:#444;padding-bottom:6px;border-bottom:1px solid #ddd}
.col-title span{color:var(--red)}
.video-thumb{left:234px;top:569px;width:142px;height:83px;background:linear-gradient(120deg,#c9c9c9,#8e8e8e 45%,#e07a9a)}
.play{left:293px;top:599px;width:24px;height:24px;border-radius:50%;background:rgba(255,255,255,.75)}
.video-text{left:234px;top:658px;width:142px;font-size:5.6px;line-height:8px;color:#666}
.post-thumb{left:386px;width:46px;height:32px;background:linear-gradient(135deg,#7a1a22,#3b5f9a)}
.post-title{left:439px;font-size:6.5px;color:#555}
.post-date{left:439px;font-size:5px;color:#888}
.post-ex{left:439px;width:90px;font-size:5px;line-height:7px;color:#aaa}
.service-list{left:541px;top:572px;list-style:none}
.service-list li{display:flex;align-items:center;gap:8px;height:13.5px;font-size:6.5px;color:#999}
/* pricing */
.pricing{left:0;top:702px;width:883px;height:158px;background:var(--red)}
.pricing-title{left:0;top:726px;width:883px;text-align:center;color:var(--white);font-size:9.5px}
.plan{top:755px;width:137px;height:72px;background:var(--red-dark);display:flex;color:var(--white)}
.plan.featured{background:transparent;border:1px solid rgba(255,255,255,.8)}
.plan-head{width:55px;display:flex;flex-direction:column;align-items:center;padding-top:11px}
.plan-name{font-family:"Oswald",sans-serif;font-weight:700;font-size:8px;margin-top:5px}
.plan-price{font-family:"Oswald",sans-serif;font-weight:700;font-size:15px;margin-top:3px}
.plan ul{list-style:none;padding-top:9px}
.plan li{font-size:5.2px;height:10.7px;display:flex;align-items:center;gap:5px;white-space:nowrap}
/* gallery */
.gallery-title{left:0;top:884px;width:883px;text-align:center;font-size:9.5px;color:#555}
.gallery-text{left:330px;top:903px;width:223px;text-align:center;font-size:5.3px;line-height:8px;color:#999}
.tile{top:936px;height:60px}
.tile.hover{background:var(--red);color:var(--white);display:flex;flex-direction:column;align-items:center;justify-content:center;font-size:6.5px;font-weight:600}
.tile.hover small{font-weight:400;font-size:5px;margin-top:2px}
/* footer */
.site-footer{left:0;top:1028px;width:883px;height:172px;background:var(--footer)}
.footer-col{left:234px;top:1028px;width:137px;height:172px;background:var(--footer-col)}
.footer-brand{left:234px;top:1046px;width:137px;display:flex;align-items:center;justify-content:center;color:var(--white);font-size:11px;font-weight:700}
.footer-rule{left:250px;top:1095px;width:104px;height:1px;background:#444}
.socials{left:270px;top:1110px;display:flex;gap:4px}
.socials span{width:9px;height:9px;border-radius:50%;background:#666}
.socials span:first-child{background:var(--red)}
.copyright{left:234px;top:1136px;width:137px;text-align:center;color:#bbb;font-size:5.2px;line-height:7.5px}
.copyright em{font-style:normal;color:var(--red-bright)}
.footer-head{top:1059px;color:#ddd;font-size:8px}
.recent{left:396px;width:98px;font-size:5.3px;color:#bbb;padding-bottom:6px;border-bottom:1px solid #3d3d3d}
.recent.first{color:var(--red-bright)}
.tweet{left:523px;width:157px;font-size:5.2px;line-height:7.5px;color:#999}
.tweet b{color:var(--red-bright);font-weight:400}
.tweet small{display:block;color:#ccc;font-size:4.5px}
</style>
</head>
<body>

<header class="abs site-header"></header>
<div class="abs brand"><span class="brand-dot"></span>brevakor</div>
<div class="abs header-mail"><i></i>info@brevakor.com</div>

<nav class="abs main-nav">
  <ul>
    <li class="active">Home</li><li>About brevakor</li><li>News/Events</li><li>Career Opertunities</li><li>Training</li><li>Blog</li><li>Testimonial</li><li>FAQ</li><li>STORE</li><li>Contact Us</li>
  </ul>
</nav>

<section class="abs hero" role="img" aria-label="Black and white photo of a woman doing push-ups beside a barbell in a gym"></section>
<div class="abs phone-tab"><span class="ico"><svg width="8" height="9" viewBox="0 0 8 9"><path d="M1.5 0.5l1.6 0.2 0.6 2-1 .8c.5 1.2 1.4 2.1 2.5 2.6l.8-1 2 .6.1 1.6c-.3.6-.9.9-1.6.8C3.6 7.5 .8 4.7.6 1.8.5 1.2.9.7 1.5.5z" fill="#fff"/></svg></span>1234 5678 90000</div>
<div class="abs slide-arrow" style="left:232px"><svg width="6" height="8"><path d="M5 1L2 4l3 3" stroke="#fff" fill="none"/></svg></div>
<div class="abs slide-arrow" style="left:657px"><svg width="6" height="8"><path d="M1 1l3 3-3 3" stroke="#fff" fill="none"/></svg></div>
<div class="abs caption-band"></div>
<div class="abs caption-tag">Lorem Ipsum is simply dummy text</div>
<p class="abs caption-text">Lorem Ipsum is simply dummy text of the printing and typesetting industry. Lorem Ipsum has been the industry's standard dummy</p>

<form class="abs request-form">
  <h3>Request a free info session Now!!!</h3>
  <p>Complete the quick form below and a brevakor trainer will contact you shortly to schedule your free personal training info session.</p>
  <div class="field">PROGRAM <span>&#8964;</span></div>
  <div class="field">DATE <svg width="6" height="6"><rect x=".5" y="1" width="5" height="4.5" fill="none" stroke="#999" stroke-width=".6"/></svg></div>
  <div class="field">NO. OF PERSON <span>&#8964;</span></div>
  <div class="field">PHONE</div>
  <div class="field msg">MESSAGE</div>
  <div class="book-btn">BOOK NOW !</div>
</form>

<h2 class="abs welcome-title">WELCOME TO BREVAKOR</h2>
<div class="abs welcome-photo" role="img" aria-label="Photo of a smiling woman in a fitness class"></div>
<p class="abs welcome-text">Lorem Ipsum is simply dummy text of the printing and typesetting industry. Lorem Ipsum has been the industry's standard dummy text ever since the 1500s, when an unknown printer took a galley of type and scrambled it to make a type specimen book. It has survived not only five centuries, but also the leap into electronic typesetting. <b>Read More</b></p>

<h3 class="abs col-title" style="left:234px;width:142px">VIDEO <span>TOUR</span></h3>
<div class="abs video-thumb" role="img" aria-label="Video still of women on spin bikes"></div>
<div class="abs play"><svg width="24" height="24"><path d="M10 7l8 5-8 5z" fill="#777"/></svg></div>
<p class="abs video-text">Lorem Ipsum is simply dummy text of the printing and typesetting industry. Lorem Ipsum has been the industry's standard dummy text ever since</p>

<h3 class="abs col-title" style="left:386px;width:142px">BLOG <span>POST</span></h3>
<div class="abs post-thumb" style="top:574px" role="img" aria-label="Blog photo of a workout"></div>
<div class="abs post-title" style="top:571px">Lorem Ipsum is simply</div>
<div class="abs post-date" style="top:582px">22 July 2014</div>
<div class="abs post-ex" style="top:590px">Lorem Ipsum is simply dummy text of the printing</div>
<div class="abs post-thumb" style="top:619px" role="img" aria-label="Blog photo of a boxing session"></div>
<div class="abs post-title" style="top:616px">Lorem Ipsum is simply</div>
<div class="abs post-date" style="top:627px">22 July 2014</div>
<div class="abs post-ex" style="top:635px">Lorem Ipsum is simply dummy text of the printing</div>

<h3 class="abs col-title" style="left:541px;width:138px">SERVICE <span>OFFERED</span></h3>
<ul class="abs service-list">
  <li><svg width="6" height="5"><path d="M.5 2.5l1.8 1.8L5.5.7" stroke="#aaa" fill="none"/></svg>Personal Training</li>
  <li><svg width="6" height="5"><path d="M.5 2.5l1.8 1.8L5.5.7" stroke="#aaa" fill="none"/></svg>Motivational Speaking</li>
  <li><svg width="6" height="5"><path d="M.5 2.5l1.8 1.8L5.5.7" stroke="#aaa" fill="none"/></svg>Bootcamp Conditioning</li>
  <li><svg width="6" height="5"><path d="M.5 2.5l1.8 1.8L5.5.7" stroke="#aaa" fill="none"/></svg>Rondalo</li>
  <li><svg width="6" height="5"><path d="M.5 2.5l1.8 1.8L5.5.7" stroke="#aaa" fill="none"/></svg>Kickboxing Cardio</li>
  <li><svg width="6" height="5"><path d="M.5 2.5l1.8 1.8L5.5.7" stroke="#aaa" fill="none"/></svg>Hip Hop Cardio</li>
</ul>

<section class="abs pricing"></section>
<h2 class="abs pricing-title">PRICING AND PLANS</h2>

<div class="abs plan" style="left:234px">
  <div class="plan-head"><svg width="14" height="14"><path d="M2 12l2-4 6-6 2 2-6 6z" fill="#2a2a2a"/></svg><span class="plan-name">STANDARD</span><span class="plan-price">$45.00</span></div>
  <ul><li>✓ Lorem Ipsum</li><li>✓ Simply dummy text</li><li>✓ Printing and typesetting</li><li>✓ Lorem Ipsum has</li><li>✓ Been the industry's</li></ul>
</div>
<div class="abs plan featured" style="left:386px">
  <div class="plan-head"><svg width="14" height="14"><path d="M7 1l1.8 4 4.2.4-3.2 2.8 1 4.2L7 10.2 3.2 12.4l1-4.2L1 5.4l4.2-.4z" fill="#2a2a2a"/></svg><span class="plan-name">ADVANCED</span><span class="plan-price">$65.00</span></div>
  <ul><li>✓ Lorem Ipsum</li><li>✓ Simply dummy text</li><li>✓ Printing and typesetting</li><li>✓ Lorem Ipsum has</li><li>✓ Been the industry's</li></ul>
</div>
<div class="abs plan" style="left:541px">
  <div class="plan-head"><svg width="14" height="14"><rect x="1" y="4" width="12" height="8" fill="#2a2a2a"/><rect x="5" y="2" width="4" height="3" fill="none" stroke="#2a2a2a"/></svg><span class="plan-name">BUSINESS</span><span class="plan-price">$95.00</span></div>
  <ul><li>✓ Lorem Ipsum</li><li>✓ Simply dummy text</li><li>✓ Printing and typesetting</li><li>✓ Lorem Ipsum has</li><li>✓ Been the industry's</li></ul>
</div>

<h2 class="abs gallery-title">GALLERY</h2>
<p class="abs gallery-text">Praesent posuere eros in quam dictum, quis dignissim odio suscipit. Integer luctus mi sit amet orci porttitor, at malesuada mauris sodales. Mauris vitae ipsum sed risus.</p>
<div class="abs tile" style="left:234px;width:106px;background:linear-gradient(135deg,#b9b9b9,#6d6d6d 60%,#d98aa0)" role="img" aria-label="Gallery photo of a woman lifting a barbell"></div>
<div class="abs tile hover" style="left:347px;width:105px">Lorem Ipsum is simply dummy<small>text of the printing</small></div>
<div class="abs tile" style="left:458px;width:107px;background:linear-gradient(135deg,#a8d6ef,#3a8bc0 55%,#e8cdb1)" role="img" aria-label="Gallery photo of a woman in a cardio class"></div>
<div class="abs tile" style="left:571px;width:107px;background:linear-gradient(135deg,#f0d7c4,#d9627e 55%,#6a6a6a)" role="img" aria-label="Gallery photo of a group on spin bikes"></div>

<footer class="abs site-footer"></footer>
<div class="abs footer-col"></div>
<div class="abs footer-brand"><span class="brand-dot"></span>brevakor</div>
<div class="abs footer-rule"></div>
<div class="abs socials" aria-label="Social links"><span></span><span></span><span></span><span></span></div>
<p class="abs copyright">Copyright © 2014 Company Name<br>All Rights Reserved.<br><em>Privacy Policy</em> | Terms &amp; Condition</p>

<h3 class="abs footer-head" style="left:396px">RECENT &nbsp;BLOGS</h3>
<div class="abs recent first" style="top:1084px">Lorem Ipsum is simply dummy</div>
<div class="abs recent" style="top:1102px">Lorem Ipsum is simply dummy</div>
<div class="abs recent" style="top:1120px">Lorem Ipsum is simply dummy</div>
<div class="abs recent" style="top:1138px">Lorem Ipsum is simply dummy</div>

<h3 class="abs footer-head" style="left:523px">GET IN TWEET</h3>
<p class="abs tweet" style="top:1084px"><b>@companyname</b> Lorem Ipsum is simply dummy text of the printing and typesetting industry<small>5 min ago</small></p>
<p class="abs tweet" style="top:1122px"><b>@companyname</b> Lorem Ipsum is simply dummy text of the printing and typesetting industry<small>5 min ago</small></p>

</body>
</html>
```